K7 Digital Stationery Design Project

We are looking to have stationary designs created for our company branding materials. We are looking for the following to be created.
1. Business Cards (front & back)
2. Letterhead
3. Envelopes #10
We are a new web design, development and marketing firm. Primary color scheme is desired to be blue/grey/white. This web start-up is owned and operated by individuals with 15+ years experience each in the industry so should not look as though it is a start-up by young/inexperienced individuals.
We build website & custom applications/software. In addition we provide the full spectrum of web marketing solutions including SEO, PPC, Social Media, Branding, Content Marketing and PR.
Please let us know if you have any questions. Looking forward to seeing all the amazing design ideas.
Attached is our logo.
Thanks!
Target Market(s)
Company will be nearly 100% business to business sales. Looking to work with companies that are already established, with a website, who want to take their website and/or online marketing efforts to the next level.
Industry/Entity Type
Marketing
Look and feel

```html
<!DOCTYPE html>
<html lang="en">
<head>
<meta charset="utf-8">
<title>K7 Digital – Envelope #10</title>
<link rel="stylesheet" href="https://fonts.googleapis.com/css2?family=Jost:wght@400;500;700&display=swap">
<style>
  :root {
    --paper: #ffffff;
    --flap-grey: #e6e7e8;
    --mid-grey: #bcbdbf;
    --dark-grey: #6d6e70;
    --ink: #414042;
    --label: #111111;
    --blue-start: #00aed9;
    --blue-end: #1b75bb;
    --hairline: #d6d7d9;
  }
  html, body {
    margin: 0;
    padding: 0;
    width: 1200px;
    height: 1000px;
    overflow: hidden;
    background: var(--paper);
  }
  .canvas {
    display: block;
    width: 1200px;
    height: 1000px;
  }
  .view-label {
    font-family: "Jost", sans-serif;
    font-weight: 400;
    font-size: 27px;
    fill: var(--label);
  }
  .brand-name {
    font-family: "Jost", sans-serif;
    font-weight: 700;
    fill: var(--ink);
  }
  .brand-tagline {
    font-family: "Jost", sans-serif;
    font-weight: 500;
    fill: var(--ink);
  }
  .flap-back { fill: var(--flap-grey); }
  .body-edge { fill: var(--paper); stroke: var(--hairline); stroke-width: 1; }
  .fold-line { stroke: var(--hairline); stroke-width: 1; fill: none; }
  .brand-dot { fill: var(--blue-start); }
</style>
</head>
<body>
<svg class="canvas" viewBox="0 0 1200 1000" xmlns="http://www.w3.org/2000/svg" role="img" aria-label="K7 Digital number 10 envelope, back and front views">
  <defs>
    <linearGradient id="brand-blue" x1="0" y1="0" x2="1" y2="0">
      <stop offset="0" stop-color="var(--blue-start)"/>
      <stop offset="1" stop-color="var(--blue-end)"/>
    </linearGradient>
    <linearGradient id="artwork-tone" x1="0" y1="0" x2="1" y2="0">
      <stop offset="0" stop-color="#8f9093"/>
      <stop offset="0.45" stop-color="#1b8fc8"/>
      <stop offset="1" stop-color="#e6e7e8"/>
    </linearGradient>
  </defs>

  <!-- View labels -->
  <text class="view-label" x="107" y="112">Envelope #10</text>
  <text class="view-label" x="215" y="313">back</text>
  <text class="view-label" x="215" y="769">Front</text>

  <!-- Back view -->
  <g class="envelope-back">
    <polygon class="flap-back" points="418,149 486,53 774,21 1050,53 1102,149"/>
    <rect class="body-edge" x="418" y="149" width="684" height="297"/>
    <rect class="back-artwork" x="418.5" y="149.5" width="340" height="296" fill="url(#artwork-tone)" role="img" aria-label="Abstract geometric artwork in grey and blue tones"/>
    <g class="brand-lockup">
      <circle class="brand-dot" cx="1000" cy="370" r="7"/>
      <text class="brand-name" x="1000" y="409" font-size="20" text-anchor="middle">K7 DIGITAL</text>
      <text class="brand-tagline" x="1000" y="420" font-size="7.5" text-anchor="middle">Web Design, Development and Marketing</text>
    </g>
  </g>

  <!-- Front view -->
  <g class="envelope-front">
    <polygon fill="url(#brand-blue)" points="418,620 486,524 774,492 1050,524 1102,620"/>
    <rect class="body-edge" x="418" y="620" width="684" height="297"/>
    <path fill="url(#brand-blue)" d="M418,620 Q470,618 486,634 L570,713 L952,713 L1036,634 Q1055,618 1102,620 Z"/>
    <line class="fold-line" x1="570" y1="713" x2="418" y2="917"/>
    <line class="fold-line" x1="952" y1="713" x2="1102" y2="917"/>
    <g class="brand-lockup">
      <circle class="brand-dot" cx="769" cy="846" r="6"/>
      <text class="brand-name" x="769" y="885" font-size="17" text-anchor="middle">K7 DIGITAL</text>
      <text class="brand-tagline" x="769" y="894" font-size="6.5" text-anchor="middle">Web Design, Development and Marketing</text>
    </g>
  </g>
</svg>
</body>
</html>
```